Business Card Design

I need a business card for my rental business. The business is named:
Cruise a Trikeway Houston
www.cruiseatrikewayhouston.com
(832) 555-0193
This will be a business card that I will leave at other businesses as advertisement so it needs to have the name, website, and phone number.
Please feel free to be creative. This is a new business so I have no designs.
Thank you very much for your time and I look forward to receiving your designs
Target Market(s)
Local rental customers
Industry/Entity Type
Business
Contact Information for Business Card
Please check out my website:
Font styles to use
Other font styles liked:
- anything creative
Colors
Designer to choose colors to be used in the design.
Requirements
Must have
- Business name, phone, website. Rentals available hourly or daily. Book online

```html
<!DOCTYPE html>
<html lang="en">
<head>
<meta charset="utf-8">
<title>Cruise a Trikeway Houston – Business Cards</title>
<link rel="stylesheet" href="https://fonts.googleapis.com/css2?family=Open+Sans:wght@400;600;700&display=swap">
<style>
  :root {
    --page-bg: #e9e6e4;
    --card-top: #f1efee;
    --brand-red: #a92225;
    --brand-dark: #221f20;
    --logo-grey: #6d6c6c;
    --text-light: #ffffff;
    --text-soft: #f1dede;
    --icon-grey: #d9c9c9;
  }
  * { box-sizing: border-box; margin: 0; padding: 0; }
  html, body { width: 1200px; height: 900px; overflow: hidden; }
  body {
    background: var(--page-bg);
    font-family: "Open Sans", Arial, sans-serif;
    position: relative;
  }
  .card {
    position: absolute;
    overflow: hidden;
    box-shadow: 0 4px 14px rgba(0,0,0,0.12);
  }
  .card-front { left: 238px; top: 62px; width: 555px; height: 343px; }
  .card-back  { left: 457px; top: 518px; width: 560px; height: 342px; }

  .card-brand {
    background: var(--card-top);
    height: 185px;
    display: flex;
    flex-direction: column;
    align-items: center;
    justify-content: center;
    text-align: center;
  }
  .card-back .card-brand { height: 187px; }
  .brand-name {
    color: var(--logo-grey);
    font-weight: 700;
    text-transform: uppercase;
    line-height: 1.08;
    letter-spacing: 1px;
  }
  .brand-name .line-one { display: block; font-size: 40px; }
  .brand-name .line-two { display: block; font-size: 36px; }

  .contact-band {
    background: var(--brand-red);
    height: 158px;
    position: relative;
    color: var(--text-light);
  }
  .person { position: absolute; left: 26px; top: 56px; }
  .person-name { font-size: 18px; font-weight: 700; text-transform: uppercase; line-height: 22px; }
  .person-role { font-size: 15px; color: var(--text-soft); line-height: 20px; }
  .divider {
    position: absolute; left: 268px; top: 64px;
    width: 1px; height: 56px; background: rgba(255,255,255,0.35);
  }
  .contact-list { position: absolute; left: 276px; top: 56px; list-style: none; }
  .contact-list li {
    display: flex; align-items: center; gap: 7px;
    font-size: 15px; line-height: 21.5px;
  }
  .contact-list svg { width: 11px; height: 11px; fill: var(--icon-grey); flex: none; }

  .promo-band {
    background: var(--brand-dark);
    height: 155px;
    position: relative;
    color: var(--text-light);
    font-size: 19px;
    text-align: center;
  }
  .promo-hours { position: absolute; left: 0; right: 0; top: 44px; }
  .promo-book {
    position: absolute; left: 0; right: 0; top: 84px;
    height: 25px; line-height: 25px;
    background: var(--brand-red);
  }
</style>
</head>
<body>

  <section class="card card-front" aria-label="Business card front">
    <div class="card-brand">
      <p class="brand-name"><span class="line-one">Cruise a</span><span class="line-two">Trikeway Houston</span></p>
    </div>
    <div class="contact-band">
      <div class="person">
        <p class="person-name">Marcus Delgado</p>
        <p class="person-role">Managing Director</p>
      </div>
      <span class="divider"></span>
      <ul class="contact-list">
        <li>
          <svg viewBox="0 0 12 12" aria-hidden="true"><path d="M1 4c0-2 2-3 3-3l1 2-1 1c1 2 2 3 4 4l1-1 2 1c0 1-1 3-3 3C4 11 1 8 1 4z"/></svg>
          (832) 555-0193
        </li>
        <li>
          <svg viewBox="0 0 12 12" aria-hidden="true"><path d="M1 3h10v7H1z M1 3l5 4 5-4" stroke="#a92225" stroke-width="0.9"/></svg>
          info@cruiseatrikewayhouston.com
        </li>
        <li>
          <svg viewBox="0 0 12 12" aria-hidden="true"><circle cx="6" cy="6" r="5"/></svg>
          www.cruiseatrikewayhouston.com
        </li>
      </ul>
    </div>
  </section>

  <section class="card card-back" aria-label="Business card back">
    <div class="card-brand">
      <p class="brand-name"><span class="line-one">Cruise a</span><span class="line-two">Trikeway Houston</span></p>
    </div>
    <div class="promo-band">
      <p class="promo-hours">Rentals available hourly or daily.</p>
      <p class="promo-book">Book online @ www.cruiseatrikewayhouston.com</p>
    </div>
  </section>

</body>
</html>
```